New brand for digital company - your chance to get creative

We need to create a brand for our new business 'Lanternfield Digital'. Please read the brief below before progressing as we are looking for some quite specific outputs.

Background

We are positioning ourselves as ‘marketing technologists’ - we're helping businesses engage with their customers in the online space.

Our tactics include branding, marketing, online management, and social media, however we are differentiating ourselves by focusing on overall strategy, not just tactics. Our tagline is ‘Online made simple’.

We have stipulated some parameters for the brand but otherwise want designers to exercise their creativity.

Requirements
Must have
• We want to see an entire concept, not just a logo.

```html
<!DOCTYPE html>
<html lang="en">
<head>
<meta charset="utf-8">
<title>Lanternfield Digital – Flyer</title>
<link rel="stylesheet" href="https://fonts.googleapis.com/css2?family=Archivo+Narrow:wght@400;700&family=Roboto:wght@400;700&display=swap">
<style>
  :root {
    --maroon: #9c1c48;
    --magenta: #d4145a;
    --orange: #f7941d;
    --green: #0a7d4c;
    --ink: #1e1e1e;
    --white: #ffffff;
    --pink: #f3a0b8;
  }
  * { margin: 0; padding: 0; box-sizing: border-box; }
  html, body { width: 848px; height: 1200px; overflow: hidden; background: var(--white); }
  .flyer {
    position: relative; width: 848px; height: 1200px; overflow: hidden;
    background: var(--white); font-family: "Archivo Narrow", "Arial Narrow", sans-serif; color: var(--ink);
  }
  .hero-photo {
    position: absolute; left: 0; top: 0; width: 848px; height: 496px;
    background:
      radial-gradient(ellipse at 78% 40%, rgba(255,255,255,.95) 0%, rgba(255,255,255,0) 45%),
      radial-gradient(ellipse at 30% 55%, rgba(120,150,220,.55) 0%, rgba(120,150,220,0) 55%),
      linear-gradient(180deg, #c9d4ef 0%, #8fa2d6 45%, #c6d0ee 75%, #eef1fb 100%);
  }
  .top-bar { position: absolute; left: 90px; top: 0; width: 667px; height: 7px; background: var(--magenta); }
  .brand-panel {
    position: absolute; left: 271px; top: 0; width: 306px; height: 192px;
    background: rgba(255,255,255,.9); border-radius: 0 0 14px 14px;
    display: flex; flex-direction: column; align-items: center; justify-content: flex-end; padding-bottom: 26px;
  }
  .brand-square { width: 58px; height: 58px; background: var(--orange); margin-bottom: 18px; }
  .brand-name { font-family: "Roboto", Arial, sans-serif; font-weight: 700; font-size: 23px; color: var(--maroon); text-transform: uppercase; letter-spacing: .2px; }
  .brand-tagline { font-family: "Roboto", Arial, sans-serif; font-weight: 700; font-size: 11.5px; color: var(--green); text-transform: uppercase; margin-top: 3px; }
  .headline { position: absolute; left: 0; top: 353px; }
  .headline-line {
    display: block; background: var(--maroon); color: var(--orange);
    font-family: "Roboto", Arial, sans-serif; font-size: 34px; line-height: 56px; padding-left: 26px;
  }
  .headline-line.first { width: 497px; }
  .headline-line.second { width: 480px; margin-top: 4px; }
  .headline-accent { color: var(--pink); }
  .divider { position: absolute; left: 0; top: 496px; width: 848px; height: 8px; background: var(--orange); }
  .body-copy { position: absolute; font-size: 14.3px; line-height: 17.7px; text-align: justify; }
  .body-copy.left { left: 26px; top: 538px; width: 376px; }
  .body-copy.right { left: 464px; top: 800px; width: 364px; }
  .pull-quote {
    position: absolute; font-family: "Roboto", Arial, sans-serif; font-size: 30px; line-height: 38px;
    text-align: justify; padding: 18px 20px;
  }
  .pull-quote.orange { left: 20px; top: 906px; width: 362px; height: 217px; background: var(--orange); color: var(--green); }
  .pull-quote.green { left: 464px; top: 544px; width: 362px; height: 218px; background: var(--green); color: var(--white); }
  .footer {
    position: absolute; left: 0; top: 1140px; width: 848px; height: 60px; background: var(--maroon);
    display: flex; align-items: center; color: var(--white);
  }
  .footer-brand { width: 112px; padding-left: 18px; display: flex; align-items: center; gap: 5px; font-family: "Roboto", Arial, sans-serif; font-weight: 700; font-size: 8px; text-transform: uppercase; line-height: 10px; }
  .footer-square { width: 12px; height: 12px; background: var(--white); flex: none; }
  .footer-text { font-family: "Roboto", Arial, sans-serif; font-weight: 700; font-size: 11.5px; padding-left: 26px; }
</style>
</head>
<body>
<div class="flyer">
  <div class="hero-photo" role="img" aria-label="Blurred photo of business people walking through a bright, glass-walled lobby in blue tones"></div>
  <div class="top-bar"></div>
  <div class="brand-panel">
    <div class="brand-square"></div>
    <div class="brand-name">Lanternfield Digital</div>
    <div class="brand-tagline">Online made simple</div>
  </div>
  <h1 class="headline">
    <span class="headline-line first">Lorem ipsum dolor sit amet</span>
    <span class="headline-line second">consectetur <span class="headline-accent">adipiscing</span> elit.</span>
  </h1>
  <div class="divider"></div>

  <p class="body-copy left">Lorem ipsum dolor sit amet, consectetur adipiscing elit. Mauris ac lectus eros. Aenean placerat eros id odio ornare vitae mollis elit adipiscing. Cras vehicula nulla a tortor tempor vel posuere leo pretium. Vivamus dolor urna, porta vitae imperdiet id, porttitor id massa. Praesent at nulla nibh, sed porta enim. Vestibulum ante ipsum primis in faucibus orci luctus et ultrices posuere cubilia Curae; Quisque pretium, sem pellentesque luctus pellentesque, urna ipsum tempor nisl, vel vehicula eros lectus eu magna. Ut a est sit amet tortor hendrerit lacinia eu sed arcu. Nulla consequat, sem at fermentum dapibus, elit leo sollicitudin mauris, vel dapibus tortor quam sit amet mi. Aliquam sollicitudin felis sit amet leo mattis eu blandit mi rhoncus.</p>

  <blockquote class="pull-quote orange">“Nulla ultrices euismod convallis. Fusce venenatis, libero ac pulvinar vestibulum.”</blockquote>
  <blockquote class="pull-quote green">“Nulla consequat, sem at fermentum dapibus, elit leo sollicitudin mauris.”</blockquote>

  <p class="body-copy right">Donec leo nisl, semper eget lacinia faucibus, ultricies non sapien. Morbi accumsan urna nec nisi rhoncus id adipiscing neque dignissim. Nunc sodales, dui non accumsan tempus, erat diam malesuada nulla, non pulvinar turpis elit a purus. Maecenas vel metus neque. Nulla ultrices euismod convallis. Fusce venenatis, libero ac pulvinar vestibulum, ante nisl mollis turpis, et dignissim erat enim sed enim. Nulla ut rhoncus ipsum. Aliquam aliquam, nunc non mollis faucibus, massa sem aliquet nibh, at imperdiet mauris sem non metus. Praesent eleifend congue risus in convallis.</p>

  <footer class="footer">
    <div class="footer-brand"><span class="footer-square"></span><span>Lanternfield Digital</span></div>
    <div class="footer-text">Lorem ipsum dolor sit amet, consectetur adipiscing elit. Mauris ac lectus eros</div>
  </footer>
</div>
</body>
</html>
```